Accounting business needs a great flyer

I need a flyer for my new business "Bright Ledger". I am an individual accountant working for himself on the Sunshine Coast in Queensland Australia. I would like to see designs that communicate reliability and trust. I believe my point of difference is that I am always available to my clients and I will cap my number of clients to ensure I can service them properly.
The main point I want to convey is that most of the time junior employees with little to no experience or unqualified employees do the tax work for the clients and a senior accountant quickly checks the work at the end but never gets to really know the clients business. Accountants in general seem to have a bad reputation for not responding to clients in a timely fashion, whether by email or phone. This is where I intend to differentiate myself. . I have also included some logo's that should go on the flyer.

Target Market(s)

Every small business

Industry/Entity Type

Public Accounting

Requirements
Must have
• Web address: www.brightledger.com.au
Phone number: 0418 592 637
Attached logos
Reference to: "Do you know who is actually doing your tax?"
Other accounting firms - use junior unqualified staff
- outsource to cheap labour countries
- use tax consultants who sometimes have had only 2 weeks training.
At Bright Ledger, a highly qualified CPA with a Masters in Taxation does your work from start to finish.
**I don't need it to say exactly this but I want the theme of the flyer to have these points in it.
Nice to have
• Something different

```html
<!DOCTYPE html>
<html lang="en">
<head>
<meta charset="utf-8">
<title>Bright Ledger – Flyer</title>
<link rel="stylesheet" href="https://fonts.googleapis.com/css2?family=Montserrat:wght@400;500;600;700;800&family=Oswald:wght@500&display=swap">
<style>
  :root {
    --orange: #f15a29;
    --headline-grey: #55595e;
    --text: #2f3236;
    --white: #ffffff;
    --band-dark: #16181b;
    --band-mid: #2a2d31;
    --badge-green: #b9cf2a;
    --badge-blue: #1ab4e6;
    --badge-navy: #0d4f9c;
    --badge-yellow: #ffd400;
  }
  * { margin: 0; padding: 0; box-sizing: border-box; }
  html, body { width: 927px; height: 1200px; overflow: hidden; background: var(--white); }
  .flyer {
    position: relative;
    width: 927px;
    height: 1200px;
    overflow: hidden;
    font-family: "Montserrat", Arial, sans-serif;
    color: var(--text);
  }
  .brand {
    position: absolute;
    top: 40px;
    right: 18px;
    width: 180px;
    text-align: center;
  }
  .brand-dot {
    width: 52px; height: 52px;
    border-radius: 50%;
    border: 3px solid var(--text);
    margin: 0 auto 12px;
  }
  .brand-name {
    font-size: 14px;
    font-weight: 600;
    letter-spacing: 3px;
    color: var(--text);
    white-space: nowrap;
  }
  .kicker {
    position: absolute;
    left: 49px; top: 113px;
    font-size: 32px;
    font-weight: 700;
    color: var(--headline-grey);
    letter-spacing: -0.3px;
  }
  .headline {
    position: absolute;
    left: 46px; top: 152px;
    font-size: 77px;
    font-weight: 800;
    color: var(--orange);
    line-height: 1;
    letter-spacing: -1px;
  }
  .intro {
    position: absolute;
    left: 51px; top: 236px;
    width: 690px;
    font-size: 17.5px;
    font-weight: 500;
    line-height: 26px;
  }
  .hero {
    position: absolute;
    left: 0; top: 330px;
    width: 927px; height: 302px;
    background: radial-gradient(ellipse at 62% 55%, var(--band-mid), var(--band-dark) 70%);
  }
  .hero-quote {
    position: absolute;
    right: 464px; top: 130px;
    text-align: right;
    color: var(--white);
    font-size: 26px;
    font-weight: 700;
    line-height: 30px;
  }
  .section-title {
    font-family: "Oswald", "Arial Narrow", sans-serif;
    font-weight: 500;
    font-size: 30px;
    line-height: 1;
    color: var(--text);
    margin-bottom: 8px;
  }
  .about {
    position: absolute;
    left: 49px; top: 666px;
    width: 420px;
    font-size: 17.5px;
    font-weight: 500;
    line-height: 27px;
  }
  .about ul, .services ul { list-style: none; }
  .about ul { margin-top: 5px; }
  .about li { line-height: 26px; padding-left: 20px; position: relative; }
  .about li::before, .services li::before {
    content: "";
    position: absolute; left: 2px; top: 11px;
    width: 6px; height: 6px;
    background: var(--text);
  }
  .services {
    position: absolute;
    left: 498px; top: 666px;
    width: 390px;
    font-size: 17.5px;
    font-weight: 500;
  }
  .services li { line-height: 26px; padding-left: 13px; position: relative; }
  .services li::before { left: 1px; width: 5px; height: 5px; top: 10px; }
  .services p { margin-top: 18px; padding-left: 4px; line-height: 26px; }
  .badges { position: absolute; left: 49px; top: 1101px; }
  .badge { position: absolute; }
  .badge-board {
    left: 0; top: 0; width: 54px; height: 54px; border-radius: 50%;
    border: 2px solid var(--text);
    background: radial-gradient(circle, var(--badge-green) 45%, var(--white) 47%);
  }
  .badge-agent {
    left: -4px; top: 57px; width: 62px;
    font-size: 6.5px; line-height: 8px; text-align: center;
  }
  .badge-cloud { left: 71px; top: 0; width: 54px; height: 54px; border-radius: 50%; background: var(--badge-blue); }
  .badge-cert {
    left: 146px; top: 0; width: 124px; height: 55px;
    background: linear-gradient(90deg, var(--badge-navy) 61%, var(--badge-yellow) 61%);
  }
  .contact {
    position: absolute;
    display: flex; align-items: flex-start; gap: 7px;
    font-size: 16px; font-weight: 500; line-height: 17px;
    white-space: nowrap;
  }
  .contact svg { flex: none; }
  .contact-phone { left: 420px; top: 1102px; }
  .contact-place { left: 420px; top: 1139px; }
  .contact-mail { left: 652px; top: 1102px; }
  .contact-web { left: 652px; top: 1136px; }
  .contact span { padding-top: 4px; }
</style>
</head>
<body>
<main class="flyer">
  <div class="brand">
    <div class="brand-dot"></div>
    <div class="brand-name">BRIGHT LEDGER</div>
  </div>

  <h2 class="kicker">do you know who is actually doing</h2>
  <h1 class="headline">YOUR TAX</h1>
  <p class="intro">Accounting firms use unqualified Tax Consultants for your tax work<br>At BrightLedger Highly qualified CPA with a Masters in Taxation does your work from start to finish</p>

  <section class="hero" role="img" aria-label="Photo of letter dice spelling TAX beside a white alarm clock on dark leather">
    <p class="hero-quote">“Save time for<br>things that<br>really matter”</p>
  </section>

  <section class="about">
    <h3 class="section-title">About Us</h3>
    <p>Bright Ledger is a Certified Practising Accounting firm based on the Sunshine Coast in Queensland.<br>Servicing clients from the Gold Coast to Noosa, in addition to online services Australia wide</p>
    <ul>
      <li>CPA Qualified</li>
      <li>Master of Taxation (Eastbrook University)</li>
      <li>Years of experience in small businesses</li>
      <li>Ledgerly Certified</li>
    </ul>
  </section>

  <section class="services">
    <h3 class="section-title">Services</h3>
    <ul>
      <li>Tax Return Preparation</li>
      <li>Financial Statement Preparation</li>
      <li>Tax Planning</li>
      <li>Tax Advice</li>
    </ul>
    <p>We are readily available for a chat when our clients need advice with regards to the tax consequences of purchasing investment properties, shares, forming a company or trust or just about anything tax related.</p>
  </section>

  <div class="badges">
    <div class="badge badge-board"></div>
    <div class="badge badge-agent">Tax agent<br>30118257</div>
    <div class="badge badge-cloud"></div>
    <div class="badge badge-cert"></div>
  </div>

  <div class="contact contact-phone">
    <svg width="26" height="26" viewBox="0 0 26 26" aria-hidden="true"><circle cx="13" cy="13" r="13" fill="var(--orange)"/><path d="M9 7c1-.6 1.6 0 2.2 1.4l.6 1.4c.3.8-.2 1.2-.8 1.7.6 1.6 1.8 2.9 3.4 3.6.5-.6.9-1.1 1.7-.8l1.5.6c1.3.5 1.900 1.2 1.3 2.2-.8 1.3-2 1.8-3.4 1.4C11.7 17.5 8.6 14.4 7.6 10.6 7.2 9.1 7.7 7.9 9 7z" fill="#fff"/></svg>
    <span>0418 592 637</span>
  </div>
  <div class="contact contact-place">
    <svg width="26" height="36" viewBox="0 0 26 36" aria-hidden="true"><path d="M13 1C6.4 1 1.5 6 1.5 12.3 1.5 20 13 35 13 35s11.5-15 11.5-22.7C24.5 6 19.6 1 13 1z" fill="var(--orange)"/><circle cx="13" cy="12.5" r="6" fill="#fff"/></svg>
    <span>Kingfisher Point,<br>Sunshine Coast, QLD</span>
  </div>
  <div class="contact contact-mail">
    <svg width="26" height="26" viewBox="0 0 26 26" aria-hidden="true"><circle cx="13" cy="13" r="13" fill="var(--orange)"/><rect x="6.5" y="8.5" width="13" height="9.5" rx="1" fill="none" stroke="#fff" stroke-width="1.8"/><path d="M7 9.5l6 4.5 6-4.5" fill="none" stroke="#fff" stroke-width="1.8"/></svg>
    <span>hello@brightledger.com.au</span>
  </div>
  <div class="contact contact-web">
    <svg width="26" height="26" viewBox="0 0 26 26" aria-hidden="true"><circle cx="13" cy="13" r="12" fill="var(--orange)"/><g fill="none" stroke="#fff" stroke-width="1.4"><circle cx="13" cy="13" r="8.5"/><ellipse cx="13" cy="13" rx="3.8" ry="8.5"/><path d="M4.5 13h17M6 8.5h14M6 17.5h14"/></g></svg>
    <span>www.brightledger.com.au</span>
  </div>
</main>
</body>
</html>
```